Geschäftspapiere für telefonische Kaltakquise in der Immobilienbranche
Zielgruppe
Wir produzieren via telefonischer Kaltakquise Leads und Termine für Immobilienmakler
Aufgabenstellung
Gute Frage, es soll schön aussehen und Kunden begeistern.

```html
<!DOCTYPE html>
<html lang="de">
<head>
<meta charset="utf-8">
<title>VOCARIS24 – Geschäftsausstattung</title>
<link href="https://fonts.googleapis.com/css2?family=Lato:ital,wght@0,300;0,400;0,700;0,900;1,700;1,900&display=swap" rel="stylesheet">
<style>
  :root{
    --magenta:#d4145a;
    --purple:#7f3f98;
    --blue:#3f6cb4;
    --grey-text:#6d6e71;
    --grey-dark:#595959;
    --paper:#f4f4f5;
    --stage:#e6e7e9;
    --sky:#e3eef8;
    --brand-gradient:linear-gradient(90deg,var(--magenta),var(--purple) 55%,var(--blue));
  }
  *{box-sizing:border-box;margin:0;padding:0}
  html,body{width:1200px;height:2400px;overflow:hidden}
  body{position:relative;background:#fff;font-family:"Lato",sans-serif;color:var(--grey-text)}
  .abs{position:absolute}

  /* hero */
  .hero-photo{left:0;top:0;width:1200px;height:675px;
    background:linear-gradient(120deg,#c9cfd4 0%,#e9e4de 40%,#f3efea 65%,#d8d3cd 100%)}
  .brand{display:flex;align-items:center;gap:12px;font-family:"Lato",sans-serif;font-weight:900;letter-spacing:.06em;color:var(--grey-text)}
  .brand-dot{border-radius:50%;background:var(--purple);flex:none}
  .hero-brand{right:40px;top:100px;font-size:58px}
  .hero-brand .brand-dot{width:58px;height:58px}
  .headline{left:580px;top:418px;font-weight:900;font-style:italic;font-size:40px;line-height:40px;
    background:var(--brand-gradient);-webkit-background-clip:text;background-clip:text;color:transparent}

  /* icons & colours */
  .section-title{font-weight:700;font-size:30px;line-height:36px;color:var(--grey-text)}
  .section-title .sub{display:block;font-weight:300;letter-spacing:.02em}
  .icons-title{left:90px;top:718px}
  .icon-row{left:458px;top:714px;display:flex;gap:57px}
  .icon-row svg{width:70px;height:70px}
  .swatches{left:0;top:817px;width:1200px;height:58px;display:flex}
  .swatches span{flex:1}
  .sw-magenta{background:var(--magenta)}
  .sw-purple{background:var(--purple)}
  .sw-blue{background:var(--blue)}
  .gradient-bar{left:0;top:886px;width:1198px;height:55px;background:var(--brand-gradient)}

  /* letterhead */
  .paper-title{left:90px;top:992px}
  .stage{left:0;top:1090px;width:1200px;height:570px;background:var(--stage)}
  .letter-front{left:210px;top:1128px;width:340px;height:484px;background:var(--paper);box-shadow:0 6px 18px rgba(0,0,0,.15)}
  .letter-front .brand{position:absolute;right:22px;top:30px;font-size:10px;gap:4px}
  .letter-front .brand-dot{width:10px;height:10px}
  .sender-line{position:absolute;left:32px;top:80px;font-size:4px;color:#888}
  .letter-tagline{position:absolute;left:32px;bottom:50px;font-size:7px;font-weight:900;font-style:italic;color:var(--magenta)}
  .letter-footer{position:absolute;left:0;bottom:0;width:100%;height:40px;background:var(--brand-gradient);color:#fff;font-size:5px;padding:7px 32px;line-height:12px}
  .letter-footer .row{display:flex;gap:26px;align-items:center}
  .letter-footer svg{width:7px;height:7px;vertical-align:-1px;margin-right:3px}
  .letter-back{left:587px;top:1275px;width:485px;height:337px;background:linear-gradient(180deg,var(--blue) 0%,var(--purple) 45%,var(--magenta) 100%);box-shadow:0 6px 18px rgba(0,0,0,.18)}

  /* lower panels */
  .cards-title{left:90px;top:1706px}
  .mail-title{left:690px;top:1706px}
  .cards-panel{left:0;top:1795px;width:600px;height:605px;background:var(--sky)}
  .mail-panel{left:600px;top:1795px;width:600px;height:605px;background:var(--grey-dark)}

  .card-back{left:222px;top:1897px;width:248px;height:169px;background:var(--brand-gradient);box-shadow:0 10px 24px rgba(0,0,0,.18);
    color:#e8e4ee;font-weight:700;font-size:21px;line-height:29px;text-align:center;padding-top:32px}
  .card{width:250px;height:170px;background:var(--paper);box-shadow:0 10px 24px rgba(0,0,0,.15);top:2124px}
  .card-general{left:45px}
  .card-personal{left:317px}
  .card .brand{position:absolute;right:14px;top:14px;font-size:14px;gap:5px}
  .card .brand-dot{width:14px;height:14px}
  .card-band{position:absolute;left:0;bottom:0;width:100%;height:14px;background:var(--brand-gradient)}
  .card-tagline{position:absolute;left:22px;top:56px;font-size:10px;line-height:12px;font-weight:900;font-style:italic;color:var(--magenta)}
  .contact-list{position:absolute;list-style:none;font-size:8px;line-height:15px;color:#9a9a9a}
  .contact-list li{display:flex;align-items:center;gap:5px}
  .contact-list svg{width:9px;height:9px;flex:none}
  .contact-list .strong{color:#333;font-weight:700}
  .card-name{position:absolute;left:22px;top:54px;font-size:12px;font-weight:700;color:var(--magenta)}
  .card-role{position:absolute;left:38px;top:68px;font-size:8px;color:#9a9a9a}

  /* email */
  .mail-window{left:627px;top:1887px;width:546px;height:428px;background:#e2e2e2;padding:30px 7px 10px}
  .mail-field{background:#fff;height:35px;margin-bottom:4px;font-size:11px;color:#333;padding:12px 8px}
  .mail-body{background:#fff;height:311px;position:relative;padding:18px 8px;font-size:11px;line-height:14px;color:#333}
  .sig-greeting{position:absolute;left:25px;top:110px;font-size:7px;font-weight:700;color:#777}
  .sig-name{position:absolute;left:25px;top:127px;font-size:12px;font-weight:700;color:var(--magenta)}
  .sig-role{position:absolute;left:42px;top:143px;font-size:8px;color:#777}
  .sig-cta{position:absolute;left:8px;top:164px;width:152px;height:35px;background:var(--brand-gradient);border-radius:0 8px 0 0;color:#fff;font-size:8px;font-weight:700;line-height:12px;padding:5px 16px}
  .sig-contacts{left:25px;top:210px}
  .mail-body .brand{position:absolute;left:26px;top:282px;font-size:10px;gap:4px}
  .mail-body .brand-dot{width:11px;height:11px}
</style>
</head>
<body>
<svg width="0" height="0" style="position:absolute" aria-hidden="true">
  <defs>
    <linearGradient id="ring" x1="0" y1="1" x2="1" y2="0">
      <stop offset="0" stop-color="#d4145a"/><stop offset=".55" stop-color="#7f3f98"/><stop offset="1" stop-color="#3f6cb4"/>
    </linearGradient>
    <symbol id="ico-phone" viewBox="0 0 24 24"><path d="M6.6 3.5l3 3.2-1.8 2.3c1 2.2 3 4.2 5.2 5.2l2.3-1.8 3.2 3-1.6 3.1C11 18 6 13 4.5 5.1z" fill="currentColor"/></symbol>
    <symbol id="ico-mail" viewBox="0 0 24 24"><rect x="3" y="6" width="18" height="12" rx="1" fill="currentColor"/><path d="M3.5 6.5l8.5 6.5 8.5-6.5" stroke="#fff" stroke-width="1.4" fill="none"/></symbol>
    <symbol id="ico-globe" viewBox="0 0 24 24"><g fill="none" stroke="currentColor" stroke-width="1.6"><circle cx="12" cy="12" r="8.5"/><ellipse cx="12" cy="12" rx="3.8" ry="8.5"/><path d="M3.5 12h17M5 7.5h14M5 16.5h14M12 3.5v17"/></g></symbol>
    <symbol id="ico-home" viewBox="0 0 24 24"><path d="M12 3.5L2.5 12h2.8v8h5v-5h3.4v5h5v-8h2.8z" fill="currentColor"/></symbol>
    <symbol id="badge" viewBox="0 0 40 40"><circle cx="20" cy="20" r="16" fill="none" stroke="url(#ring)" stroke-width="3.2" stroke-dasharray="88 13"/></symbol>
  </defs>
</svg>

<header>
  <div class="abs hero-photo" role="img" aria-label="Foto: junger Mann telefoniert lächelnd am Laptop in hellem Büro"></div>
  <div class="abs brand hero-brand"><span class="brand-dot"></span>VOCARIS24</div>
  <h1 class="abs headline">Wir liefern Leads und Termine<br>für Immobilienmakler.</h1>
</header>

<section>
  <h2 class="abs section-title icons-title">Die verwendeten Icon<br>und Farben</h2>
  <div class="abs icon-row">
    <svg viewBox="0 0 40 40" style="color:#7f3f98"><use href="#badge"/><use href="#ico-phone" x="10" y="10" width="20" height="20"/></svg>
    <svg viewBox="0 0 40 40" style="color:#7f3f98"><use href="#badge"/><use href="#ico-mail" x="10" y="10" width="20" height="20"/></svg>
    <svg viewBox="0 0 40 40" style="color:#7f3f98"><use href="#badge"/><use href="#ico-globe" x="10" y="10" width="20" height="20"/></svg>
    <svg viewBox="0 0 40 40" style="color:#9a2f7a"><use href="#badge"/><use href="#ico-home" x="10" y="9" width="20" height="20"/></svg>
  </div>
  <div class="abs swatches"><span class="sw-magenta"></span><span class="sw-purple"></span><span class="sw-blue"></span></div>
  <div class="abs gradient-bar"></div>
</section>

<section>
  <h2 class="abs section-title paper-title">Das Briefpapier<span class="sub">doppelseitig</span></h2>
  <div class="abs stage"></div>
  <div class="abs letter-front">
    <div class="brand"><span class="brand-dot"></span>VOCARIS24</div>
    <p class="sender-line">VOCARIS24 · Lindenweg 12 · Ostal-Brenning · CH-8871</p>
    <p class="letter-tagline">Wir liefern Leads und Termine für Immobilienmakler.</p>
    <div class="letter-footer">
      <div class="row"><span><svg style="color:#fff"><use href="#ico-home"/></svg>Lindenweg 12 · Ostal-Brenning · CH-8871</span></div>
      <div class="row">
        <span><svg style="color:#fff"><use href="#ico-phone"/></svg>04471 - 32958-0</span>
        <span><svg style="color:#fff"><use href="#ico-mail"/></svg>info@vocaris24.com</span>
        <span><svg style="color:#fff"><use href="#ico-globe"/></svg>vocaris24.com</span>
      </div>
    </div>
  </div>
  <div class="abs letter-back"></div>
</section>

<section>
  <h2 class="abs section-title cards-title">Die Visitenkarten<span class="sub">individuell und allgemein</span></h2>
  <h2 class="abs section-title mail-title">Die E-Mail Signatur<span class="sub">individuell</span></h2>
  <div class="abs cards-panel"></div>
  <div class="abs mail-panel"></div>

  <div class="abs card-back">Gewinnen<br>war nie<br>leichter.</div>

  <div class="abs card card-general">
    <div class="brand"><span class="brand-dot"></span>VOCARIS24</div>
    <p class="card-tagline">Wir liefern Leads und Termine<br>für Immobilienmakler.</p>
    <ul class="contact-list" style="left:24px;top:96px">
      <li><svg style="color:#7f3f98"><use href="#ico-phone"/></svg>04471 - 32958-0</li>
      <li><svg style="color:#7f3f98"><use href="#ico-mail"/></svg>info@vocaris24.com</li>
      <li class="strong"><svg style="color:#7f3f98"><use href="#ico-globe"/></svg>vocaris24.com</li>
    </ul>
    <ul class="contact-list" style="left:140px;top:96px">
      <li><svg style="color:#7f3f98"><use href="#ico-home"/></svg>Lindenweg 12,</li>
      <li style="padding-left:14px">Ostal-Brenning,</li>
      <li style="padding-left:14px">CH-8871</li>
    </ul>
    <div class="card-band"></div>
  </div>

  <div class="abs card card-personal">
    <div class="brand"><span class="brand-dot"></span>VOCARIS24</div>
    <p class="card-name">Max Mustermann</p>
    <p class="card-role">Berufsbezeichnung</p>
    <ul class="contact-list" style="left:24px;top:86px">
      <li><svg style="color:#7f3f98"><use href="#ico-phone"/></svg>04471 - 32958-0</li>
      <li><svg style="color:#7f3f98"><use href="#ico-mail"/></svg>M.Mustermann@vocaris24.com</li>
      <li class="strong"><svg style="color:#7f3f98"><use href="#ico-globe"/></svg>vocaris24.com</li>
      <li><svg style="color:#7f3f98"><use href="#ico-home"/></svg>Lindenweg 12, Ostal-Brenning, CH-8871</li>
    </ul>
    <div class="card-band"></div>
  </div>

  <div class="abs mail-window">
    <div class="mail-field">Von: M.Mustermann@vocaris24.com</div>
    <div class="mail-field">An: M.Makler@beispiel-makler.com</div>
    <div class="mail-body">
      <p>Sehr geehrter Herr Makler,<br>Vielen Dank für Ihre Anfrage (...)</p>
      <p class="sig-greeting">Mit freundlichen Grüßen</p>
      <p class="sig-name">Max Mustermann</p>
      <p class="sig-role">Berufsbezeichnung · VOCARIS24</p>
      <div class="sig-cta">Ihr Gewinn ist<br>nur einen Anruf entfernt</div>
      <ul class="contact-list sig-contacts">
        <li><svg style="color:#7f3f98"><use href="#ico-phone"/></svg>04471 - 32958-0</li>
        <li><svg style="color:#7f3f98"><use href="#ico-mail"/></svg>M.Mustermann@vocaris24.com</li>
        <li class="strong"><svg style="color:#7f3f98"><use href="#ico-globe"/></svg>vocaris24.com</li>
        <li><svg style="color:#7f3f98"><use href="#ico-home"/></svg>Lindenweg 12, Ostal-Brenning, CH-8871</li>
      </ul>
      <div class="brand"><span class="brand-dot"></span>VOCARIS24</div>
    </div>
  </div>
</section>
</body>
</html>
```